依頼詳細
封筒を渡す相手先としては、不動産会社&工務店が中心であり、TO:Bということになります。
(そのためTO:Cの目線は不要です。)

封筒だけでどうこうなる部分ではないものの、信頼して工事を任せてみようと思える名刺を作成したいと考えています。

※名刺デザインについても同単価で同時募集中です!
おそらくセットで当選することになると思いますので実質倍の単価です。
記載項目
■サイズ
角2&長3
の2パターン

■封筒記載事項
LUMIQUA株式会社(ロゴ)
所在地 埼玉県さいたま市北区宮原台5-17-3 ソレイユ館2F
電話番号 048-739-2516
FAX 048-739-2516
メールアドレス info@lumiqua.example
HPアドレス https://lumiqua.example

希望イメージ
シンプル 複雑
単色 カラフル
暗い 明るい
日常 高級
遊び心 厳粛
未来的 伝統的
女性的 男性的
希望する色
納品ファイル
• イラストレーター形式 (.ai)
• フォトショップ形式 (.psd)
補足説明

```html
<!DOCTYPE html>
<html lang="ja">
<head>
<meta charset="utf-8">
<title>LUMIQUA 長3封筒</title>
<link rel="stylesheet" href="https://fonts.googleapis.com/css2?family=Montserrat:wght@700;800&family=Noto+Sans+JP:wght@400;500;700&display=swap">
<style>
  :root {
    --navy: #1e2a5a;
    --paper: #ffffff;
    --board-light: #ececec;
    --board-mid: #dedede;
    --board-dark: #cfcfcf;
    --ink: #222a44;
    --box-line: #7a8199;
  }
  * { margin: 0; padding: 0; box-sizing: border-box; }
  html, body { width: 1200px; height: 3608px; overflow: hidden; }
  body {
    position: relative;
    background: var(--paper);
    font-family: "Noto Sans JP", sans-serif;
    color: var(--ink);
  }
  .board-bg { position: absolute; inset: 0; }
  .board-label {
    position: absolute; left: 112px; top: 86px;
    font-size: 34px; font-weight: 500; letter-spacing: 1px;
  }
  .side-label {
    position: absolute; left: 112px; top: 262px;
    font-size: 20px; font-weight: 400;
  }
  .envelope {
    position: absolute; left: 260px; width: 680px;
    background: var(--paper);
    box-shadow: 0 14px 36px rgba(0,0,0,0.18);
    overflow: hidden;
  }
  .envelope--front { top: 220px; height: 1500px; }
  .envelope--back { top: 2060px; height: 1460px; }
  .flap { position: absolute; left: 0; top: 0; width: 680px; }
  .brand {
    display: flex; align-items: center; gap: 12px;
    font-family: "Montserrat", sans-serif; font-weight: 800;
    letter-spacing: 1px;
  }
  .brand__mark { width: 28px; height: 28px; background: currentColor; }
  .flap__brand {
    position: absolute; left: 0; right: 0; justify-content: center;
    color: var(--paper); font-size: 28px;
  }
  .flap__brand--inverted { top: 32px; transform: rotate(180deg); }
  .flap__brand--upright { top: 84px; }
  .postcode {
    position: absolute; top: 236px; right: 52px;
    display: flex; align-items: center;
  }
  .postcode__box { width: 40px; height: 40px; border: 2px solid var(--box-line); margin-left: -2px; }
  .postcode__box--light { border-color: #b6bac8; }
  .postcode__dash { width: 14px; height: 2px; background: var(--box-line); margin: 0 4px; }
  .sender { position: absolute; left: 48px; top: 1316px; }
  .sender__brand { color: var(--navy); font-size: 40px; }
  .sender__brand .brand__mark { width: 36px; height: 36px; }
  .sender__info { margin-top: 14px; font-size: 14px; line-height: 24px; font-weight: 500; }
  .sender__row { display: flex; gap: 20px; }
  .sender__item { display: flex; align-items: center; gap: 6px; white-space: nowrap; }
  .icon { width: 13px; height: 13px; fill: var(--navy); }
  .footer-band {
    position: absolute; left: 0; bottom: 0; width: 100%; height: 48px;
    background: var(--navy); color: var(--paper);
    display: flex; align-items: center; justify-content: center;
    font-size: 13px; letter-spacing: 0.5px;
  }
  .back-center {
    position: absolute; left: 0; right: 0; top: 600px;
    display: flex; flex-direction: column; align-items: center;
  }
  .back-center__mark { width: 52px; height: 52px; background: var(--navy); }
  .back-center__name {
    margin-top: 18px; font-family: "Montserrat", sans-serif; font-weight: 800;
    font-size: 38px; color: var(--navy); letter-spacing: 1px;
  }
  .back-center__url { margin-top: 12px; font-size: 12px; color: var(--ink); }
</style>
</head>
<body>
  <svg class="board-bg" width="1200" height="3608" viewBox="0 0 1200 3608" aria-hidden="true">
    <polygon points="1200,560 1200,1300 400,1300" fill="var(--board-mid)"/>
    <polygon points="0,1240 1200,600 1200,1900 0,1900" fill="var(--board-dark)"/>
    <rect x="0" y="1900" width="1200" height="1708" fill="var(--board-light)"/>
    <polygon points="0,3180 1200,3260 1200,3608 0,3608" fill="#f6f6f6"/>
  </svg>

  <p class="board-label">長 3 封筒 120 × 235mm</p>
  <p class="side-label">front</p>

  <section class="envelope envelope--front">
    <svg class="flap" height="100" viewBox="0 0 680 100" aria-hidden="true">
      <rect width="680" height="100" fill="var(--navy)"/>
    </svg>
    <div class="brand flap__brand flap__brand--inverted"><span class="brand__mark"></span>LUMIQUA</div>

    <div class="postcode">
      <span class="postcode__box"></span><span class="postcode__box"></span><span class="postcode__box"></span>
      <span class="postcode__dash"></span>
      <span class="postcode__box postcode__box--light"></span><span class="postcode__box postcode__box--light"></span><span class="postcode__box postcode__box--light"></span><span class="postcode__box postcode__box--light"></span>
    </div>

    <div class="sender">
      <div class="brand sender__brand"><span class="brand__mark"></span>LUMIQUA</div>
      <div class="sender__info">
        <div class="sender__row">
          <span class="sender__item"><svg class="icon" viewBox="0 0 14 14"><path d="M7 0a5 5 0 0 0-5 5c0 4 5 9 5 9s5-5 5-9a5 5 0 0 0-5-5zm0 7a2 2 0 1 1 0-4 2 2 0 0 1 0 4z"/></svg>〒331-0057 埼玉県さいたま市北区宮原台5-17-3 ソレイユ館2F</span>
        </div>
        <div class="sender__row">
          <span class="sender__item"><svg class="icon" viewBox="0 0 14 14"><path d="M3 0l3 3-2 2c1 2 3 4 5 5l2-2 3 3-2 3C6 14 0 8 0 3z"/></svg>048-739-2516</span>
          <span class="sender__item"><svg class="icon" viewBox="0 0 14 14"><rect x="1" y="5" width="12" height="8"/><rect x="3" y="1" width="8" height="4" fill="none" stroke="var(--navy)" stroke-width="1.5"/></svg>048-739-2516</span>
          <span class="sender__item"><svg class="icon" viewBox="0 0 14 14"><path d="M1 2h12v10H1z M1 3l6 5 6-5" fill="none" stroke="var(--navy)" stroke-width="1.5"/></svg>info@lumiqua.example</span>
        </div>
      </div>
    </div>

    <div class="footer-band">https://lumiqua.example</div>
  </section>

  <section class="envelope envelope--back">
    <svg class="flap" height="200" viewBox="0 0 680 200" aria-hidden="true">
      <polygon points="0,0 680,0 620,200 60,200" fill="var(--navy)"/>
    </svg>
    <div class="brand flap__brand flap__brand--upright"><span class="brand__mark"></span>LUMIQUA</div>

    <div class="back-center">
      <span class="back-center__mark"></span>
      <span class="back-center__name">LUMIQUA</span>
      <span class="back-center__url">https://lumiqua.example</span>
    </div>
  </section>
</body>
</html>
```